Personal Tax Specialists Banner

We need banner adverts for a personal tax firm. We specialise in Luxembourg, US and UK personal taxation. The banner should be modern, cool, simple and illustrated.

Banner should highlight "Personal Taxation Specialists" and the countries that we specialise in, "Luxembourg", "US" and "UK".

Target Market(s)

Individuals looking for assistance with tax return preparation.

Industry/Entity Type

Finance And Accounting

Colors

Designer to choose colors to be used in the design.

Requirements
Must have
• Output in GIF.
• The main banner size is 980 x 120 and some smaller square banners (300 x 300)
• Button to link back to website www.corvinfiling.com
Nice to have
• We would like an illustrated design if possible.

```html
<!DOCTYPE html>
<html lang="en">
<head>
<meta charset="utf-8">
<title>Corvin Tax &amp; Consulting – Banner Set</title>
<link href="https://fonts.googleapis.com/css2?family=Montserrat:wght@500;600;700&family=Roboto+Condensed:wght@400;500;700&display=swap" rel="stylesheet">
<style>
  :root {
    --stage: #000000;
    --maroon: #740033;
    --charcoal: #4b4b4b;
    --bar: #585858;
    --white: #ffffff;
    --ring: #8c8c8c;
    --concrete-light: #d6d6d6;
    --concrete-dark: #b7b7b7;
    --figure-light: #e4e4e4;
    --figure-dark: #8a8a8a;
  }
  * { box-sizing: border-box; margin: 0; padding: 0; }
  html, body { width: 1200px; height: 1000px; overflow: hidden; background: var(--stage); }
  body { position: relative; font-family: "Montserrat", Arial, sans-serif; }

  .size-label {
    position: absolute; left: 0; width: 1200px; text-align: center;
    color: var(--white); font-weight: 700; font-size: 31px; letter-spacing: -0.5px;
  }
  .size-label--leaderboard { top: 181px; }
  .size-label--square { top: 471px; }

  .banner {
    position: absolute; overflow: hidden;
    background: radial-gradient(circle at 30% 40%, var(--concrete-light), var(--concrete-dark));
  }
  .banner--leaderboard { left: 110px; top: 250px; width: 980px; height: 120px; }
  .banner--square { left: 450px; top: 540px; width: 300px; height: 300px; }

  .disc { position: absolute; border-radius: 50%; display: flex; align-items: center; justify-content: center; text-align: center; }
  .disc--charcoal { background: var(--charcoal); color: var(--white); }
  .disc--maroon { background: var(--maroon); color: var(--white); }
  .disc--white { background: var(--white); }
  .dot { position: absolute; border-radius: 50%; }
  .dot--charcoal { background: var(--charcoal); }
  .dot--maroon { background: var(--maroon); }
  .dot--white { background: var(--white); }

  .brand-panel { position: absolute; background: var(--white); }
  .brand { position: absolute; display: flex; align-items: center; color: var(--maroon); font-weight: 500; z-index: 2; }
  .brand-mark { border: 3px solid var(--ring); border-radius: 50%; flex: none; }
  .brand-name { display: flex; flex-direction: column; align-items: flex-end; }
  .brand-name__main { line-height: 1; letter-spacing: 0.5px; }
  .brand-name__sub { line-height: 1; letter-spacing: 0.3px; }

  .country-bar {
    position: absolute; background: var(--bar); color: var(--white);
    font-weight: 700; display: flex; align-items: center; white-space: nowrap; z-index: 2;
  }
  .illustration { position: absolute; background: linear-gradient(180deg, var(--figure-light) 0%, var(--figure-dark) 55%, var(--maroon) 100%); }

  .web-address { font-family: "Roboto Condensed", Arial, sans-serif; color: var(--maroon); font-weight: 500; position: absolute; white-space: nowrap; }
  .specialist { font-weight: 600; line-height: 1.3; }
  .question { font-family: "Roboto Condensed", Arial, sans-serif; font-weight: 700; }

  /* Leaderboard */
  .banner--leaderboard .brand-panel { left: 0; top: 0; width: 290px; height: 120px; }
  .banner--leaderboard .brand-curve { left: 180px; top: -60px; width: 120px; height: 240px; }
  .banner--leaderboard .brand { left: 12px; top: 8px; gap: 14px; }
  .banner--leaderboard .brand-mark { width: 76px; height: 76px; }
  .banner--leaderboard .brand-name__main { font-size: 37px; }
  .banner--leaderboard .brand-name__sub { font-size: 14px; margin-top: 3px; }
  .banner--leaderboard .country-bar { left: 0; top: 91px; width: 270px; height: 29px; padding-left: 22px; gap: 13px; font-size: 16px; }
  .banner--leaderboard .illustration { left: 270px; top: 0; width: 126px; height: 120px; border-radius: 60px 60px 0 0; }

  /* Square */
  .banner--square .brand-panel { left: 82px; top: 0; width: 218px; height: 80px; }
  .banner--square .brand { left: 84px; top: 6px; gap: 10px; }
  .banner--square .brand-mark { width: 64px; height: 64px; }
  .banner--square .brand-name__main { font-size: 29px; }
  .banner--square .brand-name__sub { font-size: 12px; margin-top: 3px; }
  .banner--square .country-bar { left: 85px; top: 72px; width: 215px; height: 24px; padding-left: 12px; gap: 6px; font-size: 14px; }
  .banner--square .illustration { left: 0; top: 20px; width: 100px; height: 280px; border-radius: 50px 50px 0 0; }
</style>
</head>
<body>

<div class="size-label size-label--leaderboard">980x120</div>

<section class="banner banner--leaderboard" aria-label="Leaderboard banner 980 by 120">
  <div class="brand-panel"></div>
  <div class="brand-panel disc brand-curve"></div>
  <div class="illustration" role="img" aria-label="Illustrated tax consultant with glasses in a maroon jacket, hand raised to her chin"></div>
  <div class="brand">
    <span class="brand-mark"></span>
    <span class="brand-name"><span class="brand-name__main">CORVIN</span><span class="brand-name__sub">TAX &amp; CONSULTING</span></span>
  </div>
  <div class="country-bar"><span>US</span><span>•</span><span>UK</span><span>•</span><span>LUXEMBOURG</span></div>

  <span class="dot dot--charcoal" style="left:393px;top:14px;width:8px;height:8px"></span>
  <span class="dot dot--charcoal" style="left:406px;top:18px;width:14px;height:14px"></span>
  <div class="disc disc--charcoal question" style="left:413px;top:14px;width:116px;height:116px;font-size:21px">Brexit?</div>
  <span class="dot dot--maroon" style="left:545px;top:86px;width:22px;height:22px"></span>
  <span class="dot dot--maroon" style="left:532px;top:106px;width:10px;height:10px"></span>
  <div class="disc disc--maroon specialist" style="left:565px;top:-55px;width:210px;height:210px;font-size:16px;padding-top:46px">UK<br>PERSONAL TAX<br>SPECIALIST</div>
  <span class="dot dot--white" style="left:780px;top:5px;width:10px;height:10px"></span>
  <span class="dot dot--white" style="left:796px;top:16px;width:18px;height:18px"></span>
  <div class="disc disc--white" style="left:795px;top:8px;width:178px;height:178px"></div>
  <span class="web-address" style="left:815px;top:74px;font-size:24px">corvinfiling.com</span>
</section>

<div class="size-label size-label--square">300x300</div>

<section class="banner banner--square" aria-label="Square banner 300 by 300">
  <div class="illustration" role="img" aria-label="Illustrated tax consultant with glasses in a maroon jacket, hand raised to her chin"></div>
  <span class="dot dot--charcoal" style="left:6px;top:4px;width:12px;height:12px"></span>
  <span class="dot dot--charcoal" style="left:20px;top:12px;width:8px;height:8px"></span>
  <div class="brand-panel"></div>
  <div class="brand">
    <span class="brand-mark"></span>
    <span class="brand-name"><span class="brand-name__main">CORVIN</span><span class="brand-name__sub">TAX &amp; CONSULTING</span></span>
  </div>
  <div class="country-bar"><span>US</span><span>•</span><span>UK</span><span>•</span><span>LUXEMBOURG</span></div>

  <span class="dot dot--charcoal" style="left:92px;top:112px;width:8px;height:8px"></span>
  <span class="dot dot--charcoal" style="left:102px;top:112px;width:14px;height:14px"></span>
  <div class="disc disc--charcoal question" style="left:98px;top:110px;width:100px;height:100px;font-size:13px;line-height:1.35">cross-border<br>worker</div>
  <span class="dot dot--maroon" style="left:256px;top:112px;width:18px;height:18px"></span>
  <span class="dot dot--maroon" style="left:276px;top:106px;width:8px;height:8px"></span>
  <div class="disc disc--white" style="left:80px;top:210px;width:176px;height:176px"></div>
  <div class="disc disc--maroon specialist" style="left:177px;top:130px;width:126px;height:126px;font-size:11px">LUXEMBOURG<br>PERSONAL TAX<br>SPECIALIST</div>
  <span class="web-address" style="left:100px;top:264px;font-size:22px">corvinfiling.com</span>
  <span class="dot dot--white" style="left:254px;top:272px;width:18px;height:18px"></span>
  <span class="dot dot--white" style="left:278px;top:284px;width:12px;height:12px"></span>
</section>

</body>
</html>
```